iPhone iOS 7 App For Managing Tasks/Photos for Internal Company Use

We need an app design that displays company objectives and task, and provides the interface for employees to complete a task by uploading a photo and adding comments.

Please see attached mock up sketches as a rough guideline

Final delivery of files must contain PSD, and all layers/objects sliced both is PSD and PNG files

Target Market(s)

This is a tool for internal employee use

Industry/Entity Type

It Company

Requirements
Must have
• Must include logo, and match the colour scheme
Use iPhone iOS 7 Style

```html
<!DOCTYPE html>
<html lang="en">
<head>
<meta charset="utf-8">
<title>Norvane Tasks – iOS 7 App Screens</title>
<link href="https://fonts.googleapis.com/css2?family=Open+Sans:wght@400;600;700&display=swap" rel="stylesheet">
<style>
:root{
  --stage:#e8492a;
  --stage-glow:#f27a45;
  --screen:#a8bbc5;
  --screen-light:#bccbd3;
  --bar:#eef1f3;
  --white:#ffffff;
  --ink:#3b4c53;
  --teal:#4b6267;
  --accent:#e8523a;
  --row:#cfd9de;
  --row-dark:#98abb4;
  --line:#7f949d;
}
*{box-sizing:border-box;margin:0;padding:0}
html,body{width:1200px;height:699px;overflow:hidden}
body{
  font-family:"Open Sans",Arial,sans-serif;color:var(--ink);
  background:radial-gradient(ellipse at 22% 8%,var(--stage-glow) 0,var(--stage) 45%);
  position:relative;
}
.screen{
  position:absolute;top:163px;width:210px;height:373px;
  background:linear-gradient(180deg,var(--screen-light),var(--screen));
  box-shadow:0 10px 26px rgba(90,20,0,.35);overflow:hidden;
}
.s1{left:27px}.s2{left:261px}.s3{left:495px}.s4{left:729px}.s5{left:963px}
.status{height:13px;background:var(--bar);font-size:6.5px;font-weight:600;display:flex;justify-content:space-between;align-items:center;padding:0 6px}
.app-header{height:28px;background:var(--white);display:flex;align-items:center;justify-content:center;gap:5px;box-shadow:0 1px 3px rgba(0,0,0,.15)}
.brand-dot{width:9px;height:9px;border-radius:50%;background:var(--accent)}
.brand-name{font-size:9.5px;font-weight:700;color:var(--teal)}
.brand-sub{font-size:9.5px;font-weight:700;color:var(--teal)}

.nav{position:absolute;left:0;right:0;bottom:0;height:56px;display:flex;justify-content:space-around;padding:0 8px}
.nav::before{content:"";position:absolute;left:28px;right:28px;top:19px;height:3px;background:var(--teal)}
.nav-item{position:relative;display:flex;flex-direction:column;align-items:center;gap:3px;padding-top:8px;font-size:7.5px;font-weight:600;color:var(--ink)}
.nav-icon{width:23px;height:23px;border-radius:50%;background:#dfe5e8;border:2px solid var(--teal);display:flex;align-items:center;justify-content:center}
.nav-icon svg{width:12px;height:12px;fill:var(--teal)}

/* login */
.signin{position:absolute;left:32px;right:32px;top:150px}
.signin-title{background:var(--white);text-align:center;font-size:7.5px;font-weight:600;padding:6px 0;letter-spacing:.3px}
.field{background:var(--teal);color:#e5ecee;font-size:7px;padding:6px 10px;border-top:1px solid #6d8388;display:flex;align-items:center;gap:6px}
.field svg{width:7px;height:7px;fill:#e5ecee}
.login-btn{background:var(--accent);color:var(--white);text-align:center;font-size:7px;font-weight:600;padding:7px 0}

/* news */
.news{position:absolute;left:6px;right:6px;top:50px;height:252px;background:var(--white);border-radius:2px}
.tabs{display:flex;gap:2px;padding:2px 3px;font-size:5.5px}
.tab{background:#e6ebee;padding:1px 4px}
.tab.active{background:var(--row)}
.news-item{display:flex;gap:6px;padding:6px 8px;border-bottom:1px solid #e4e9ec}
.avatar{flex:0 0 24px;height:24px;border-radius:50%;background:radial-gradient(circle at 50% 40%,#c89a7c,#6e4e3c)}
.news-name{font-size:9px;font-weight:600}
.news-text{font-size:4.6px;line-height:1.35;color:#6b7a80;margin-top:1px}
.news-time{font-size:5.5px;color:#6b7a80;margin-top:2px}
.scroll{position:absolute;right:3px;top:100px;width:3px;height:22px;background:#9aa9b0;border-radius:2px}

/* objectives */
.select{position:absolute;left:38px;right:24px;top:96px;height:20px;background:linear-gradient(#eef2f4,#cdd7dc);border-radius:2px;display:flex;align-items:center;gap:5px;padding:0 7px;font-size:7px;font-weight:600;box-shadow:0 1px 2px rgba(0,0,0,.2)}
.select .chev{margin-left:auto;width:7px;height:7px}
.s4 .select{left:34px;right:28px;top:86px}
.list{position:absolute;left:38px;right:24px;top:124px}
.s4 .list{left:34px;right:28px;top:120px}
.obj{height:21px;background:linear-gradient(#dfe6ea,#bccad1);border-bottom:1px solid #8fa3ac;font-size:7px;font-weight:600;display:flex;align-items:center;padding-left:22px}
.obj.selected{background:linear-gradient(#a6b8c0,#8ea3ad)}
.task{height:19px;background:var(--white);border-bottom:1px solid #ccd6db;font-size:5.5px;display:flex;align-items:center;justify-content:space-between;padding:0 8px 0 14px;margin:0 3px}
.task svg{width:9px;height:9px;fill:none;stroke:var(--accent);stroke-width:2.2}
.tasks{padding:3px 0;background:#dfe6ea}

/* upload */
.ring{position:absolute;left:62px;top:84px;width:86px;height:86px}
.ring-label{position:absolute;left:62px;top:84px;width:86px;height:86px;display:flex;flex-direction:column;align-items:center;justify-content:center;font-size:6px;font-weight:600;gap:2px}
.ring-label span.cloud{width:12px;height:12px;border-radius:50%;background:var(--accent);display:flex;align-items:center;justify-content:center}
.comments{position:absolute;left:26px;right:18px;top:190px;height:60px;background:#96aab3;border:1px solid #899ea8;font-size:7.5px;padding:5px 6px}
.save{position:absolute;left:66px;top:262px;background:var(--white);border-radius:9px;font-size:6px;font-weight:700;padding:3px 7px;box-shadow:0 1px 2px rgba(0,0,0,.25)}
</style>
</head>
<body>

<!-- Sign in -->
<section class="screen s1" aria-label="Sign in screen">
  <div class="status"><span>●●●○○ NOVA</span><span>4:21 PM</span><span>100%</span></div>
  <header class="app-header"><span class="brand-dot"></span><span class="brand-name">Norvane</span><span class="brand-sub">COMPANY NAME</span></header>
  <div class="signin">
    <div class="signin-title">SIGN IN TO CONTINUE</div>
    <div class="field"><svg viewBox="0 0 10 10"><circle cx="5" cy="3" r="2.4"/><path d="M0 10c0-3 2.2-4.5 5-4.5S10 7 10 10z"/></svg>Email</div>
    <div class="field"><svg viewBox="0 0 10 10"><circle cx="5" cy="3.5" r="3"/><rect x="4.3" y="6" width="1.4" height="4"/></svg>Password</div>
    <div class="login-btn">LOG IN</div>
  </div>
</section>

<!-- News -->
<section class="screen s2" aria-label="News screen">
  <div class="status"><span>●●●○○ NOVA</span><span>4:21 PM</span><span>100%</span></div>
  <header class="app-header"><span class="brand-dot"></span><span class="brand-name">Norvane</span><span class="brand-sub">COMPANY NAME</span></header>
  <div class="news">
    <div class="tabs"><span class="tab active">All News</span><span class="tab">Old News</span></div>
    <div class="news-item"><div class="avatar" role="img" aria-label="Profile photo of Dana Ruiz"></div><div><div class="news-name">Dana Ruiz</div><div class="news-text">Quarterly targets updated for the northern team today.</div><div class="news-time">1:50pm</div></div></div>
    <div class="news-item"><div class="avatar" role="img" aria-label="Profile photo of Mira Kovac"></div><div><div class="news-name">Mira Kovac</div><div class="news-text">New site inspection photos are due before Friday noon.</div><div class="news-time">1:45pm</div></div></div>
    <div class="news-item"><div class="avatar" role="img" aria-label="Profile photo of Wes Porter"></div><div><div class="news-name">Wes Porter</div><div class="news-text">Please review the updated safety checklist this week.</div><div class="news-time">12:15pm</div></div></div>
    <div class="news-item"><div class="avatar" role="img" aria-label="Profile photo of Noel Grant"></div><div><div class="news-name">Noel Grant</div><div class="news-text">Team meeting moved to Thursday in room four.</div><div class="news-time">9:40am</div></div></div>
    <div class="scroll"></div>
  </div>
  <nav class="nav">
    <div class="nav-item"><span class="nav-icon"><svg viewBox="0 0 12 12"><path d="M6 1 0 6h2v5h3V8h2v3h3V6h2z"/></svg></span>Home</div>
    <div class="nav-item"><span class="nav-icon"><svg viewBox="0 0 12 12"><path d="M6 1a5 5 0 1 0 0 10A5 5 0 0 0 6 1zm0 2a3 3 0 1 1 0 6 3 3 0 0 1 0-6zm0 2a1 1 0 1 0 0 2 1 1 0 0 0 0-2z"/></svg></span>Objectives</div>
    <div class="nav-item"><span class="nav-icon"><svg viewBox="0 0 12 12"><path d="M9 1l2 2-6 6-3 1 1-3z"/></svg></span>News</div>
    <div class="nav-item"><span class="nav-icon"><svg viewBox="0 0 12 12"><path d="M1 1h6v2H3v6h4v2H1zM8 3l3 3-3 3V7H5V5h3z"/></svg></span>Log Out</div>
  </nav>
</section>

<!-- Objectives -->
<section class="screen s3" aria-label="Objectives screen">
  <div class="status"><span>●●●○○ NOVA</span><span>4:21 PM</span><span>100%</span></div>
  <header class="app-header"><span class="brand-dot"></span><span class="brand-name">Norvane</span><span class="brand-sub">COMPANY NAME</span></header>
  <div class="select"><svg width="10" height="10" viewBox="0 0 12 12" fill="#4b6267"><path d="M6 1a5 5 0 1 0 0 10A5 5 0 0 0 6 1zm0 2a3 3 0 1 1 0 6 3 3 0 0 1 0-6z"/></svg>Select An Objective<svg class="chev" viewBox="0 0 8 8"><path d="M1 2.5 4 5.5 7 2.5" fill="none" stroke="#4b6267" stroke-width="1.4"/></svg></div>
  <div class="list">
    <div class="obj">Objective 1</div>
    <div class="obj selected">Objective 2</div>
    <div class="obj">Objective 3</div>
    <div class="obj">Objective 4</div>
  </div>
  <nav class="nav">
    <div class="nav-item"><span class="nav-icon"><svg viewBox="0 0 12 12"><path d="M6 1 0 6h2v5h3V8h2v3h3V6h2z"/></svg></span>Home</div>
    <div class="nav-item"><span class="nav-icon"><svg viewBox="0 0 12 12"><path d="M6 1a5 5 0 1 0 0 10A5 5 0 0 0 6 1zm0 2a3 3 0 1 1 0 6 3 3 0 0 1 0-6zm0 2a1 1 0 1 0 0 2 1 1 0 0 0 0-2z"/></svg></span>Objectives</div>
    <div class="nav-item"><span class="nav-icon"><svg viewBox="0 0 12 12"><path d="M9 1l2 2-6 6-3 1 1-3z"/></svg></span>News</div>
    <div class="nav-item"><span class="nav-icon"><svg viewBox="0 0 12 12"><path d="M1 1h6v2H3v6h4v2H1zM8 3l3 3-3 3V7H5V5h3z"/></svg></span>Log Out</div>
  </nav>
</section>

<!-- Tasks -->
<section class="screen s4" aria-label="Tasks screen">
  <div class="status"><span>●●●○○ NOVA</span><span>4:21 PM</span><span>100%</span></div>
  <header class="app-header"><span class="brand-dot"></span><span class="brand-name">Norvane</span><span class="brand-sub">COMPANY NAME</span></header>
  <div class="select"><svg width="10" height="10" viewBox="0 0 12 12" fill="#4b6267"><path d="M6 1a5 5 0 1 0 0 10A5 5 0 0 0 6 1zm0 2a3 3 0 1 1 0 6 3 3 0 0 1 0-6z"/></svg>Select An Objective<svg class="chev" viewBox="0 0 8 8"><path d="M1 2.5 4 5.5 7 2.5" fill="none" stroke="#4b6267" stroke-width="1.4"/></svg></div>
  <div class="list">
    <div class="obj">Objective 1</div>
    <div class="obj selected">Objective 2</div>
    <div class="tasks">
      <div class="task">Task 1<svg viewBox="0 0 10 10"><path d="M1 5l3 3 5-7"/></svg></div>
      <div class="task">Task 2<svg viewBox="0 0 10 10"><path d="M1 5l3 3 5-7"/></svg></div>
      <div class="task">Task 3<svg viewBox="0 0 10 10"><path d="M1 5l3 3 5-7"/></svg></div>
      <div class="task">Task 4</div>
    </div>
    <div class="obj">Objective 3</div>
    <div class="obj">Objective 4</div>
  </div>
  <nav class="nav">
    <div class="nav-item"><span class="nav-icon"><svg viewBox="0 0 12 12"><path d="M6 1 0 6h2v5h3V8h2v3h3V6h2z"/></svg></span>Home</div>
    <div class="nav-item"><span class="nav-icon"><svg viewBox="0 0 12 12"><path d="M6 1a5 5 0 1 0 0 10A5 5 0 0 0 6 1zm0 2a3 3 0 1 1 0 6 3 3 0 0 1 0-6zm0 2a1 1 0 1 0 0 2 1 1 0 0 0 0-2z"/></svg></span>Objectives</div>
    <div class="nav-item"><span class="nav-icon"><svg viewBox="0 0 12 12"><path d="M9 1l2 2-6 6-3 1 1-3z"/></svg></span>News</div>
    <div class="nav-item"><span class="nav-icon"><svg viewBox="0 0 12 12"><path d="M1 1h6v2H3v6h4v2H1zM8 3l3 3-3 3V7H5V5h3z"/></svg></span>Log Out</div>
  </nav>
</section>

<!-- Upload -->
<section class="screen s5" aria-label="Upload screen">
  <div class="status"><span>●●●○○ NOVA</span><span>4:21 PM</span><span>100%</span></div>
  <header class="app-header"><span class="brand-dot"></span><span class="brand-name">Norvane</span><span class="brand-sub">COMPANY NAME</span></header>
  <svg class="ring" viewBox="0 0 86 86">
    <circle cx="43" cy="43" r="42" fill="#fff"/>
    <circle cx="43" cy="43" r="33" fill="none" stroke="#dfe4e7" stroke-width="6"/>
    <circle cx="43" cy="43" r="33" fill="none" stroke="#e8523a" stroke-width="6" stroke-dasharray="130 210" transform="rotate(-90 43 43)"/>
    <circle cx="43" cy="43" r="27" fill="#eef1f3"/>
  </svg>
  <div class="ring-label"><span class="cloud"><svg width="7" height="7" viewBox="0 0 8 8"><path d="M4 1 1 4h2v3h2V4h2z" fill="#fff"/></svg></span>Uploading Image</div>
  <div class="comments">Comments</div>
  <div class="save">Save &amp; Complete</div>
  <nav class="nav">
    <div class="nav-item"><span class="nav-icon"><svg viewBox="0 0 12 12"><path d="M6 1 0 6h2v5h3V8h2v3h3V6h2z"/></svg></span>Home</div>
    <div class="nav-item"><span class="nav-icon"><svg viewBox="0 0 12 12"><path d="M6 1a5 5 0 1 0 0 10A5 5 0 0 0 6 1zm0 2a3 3 0 1 1 0 6 3 3 0 0 1 0-6zm0 2a1 1 0 1 0 0 2 1 1 0 0 0 0-2z"/></svg></span>Objectives</div>
    <div class="nav-item"><span class="nav-icon"><svg viewBox="0 0 12 12"><path d="M9 1l2 2-6 6-3 1 1-3z"/></svg></span>News</div>
    <div class="nav-item"><span class="nav-icon"><svg viewBox="0 0 12 12"><path d="M1 1h6v2H3v6h4v2H1zM8 3l3 3-3 3V7H5V5h3z"/></svg></span>Log Out</div>
  </nav>
</section>

</body>
</html>
```